Atelier Marrow Architecture business card

We need to update our business card. We do high end custom residential, hospitality, and wellness architecture. We focus on creating unique spaces and design around the five senses, believing that architecture's true impact is not on our surroundings, but within us. We would like to see designs are instill a sense of calm awe. They should be crisp, fresh, clean, authentic, & contemporary without being sterile, overworked, or harsh. White space is important. Alternative materials are an option if natural. We have created our own logo and would like designs to incorporate it. However, we are willing to see alternatives if the logo becomes a stumbling block and you have an alternate you suggest. Card must have the following information:
Atelier Marrow Architecture, Inc.
728 Holloway Ct. NE Atlanta, GA 30318
Marcus T. Whitcombe, AIA, NCARB, LEED AP BD+C
ateliermarrow.example

Target Market(s)

Higher net worth individuals with an appreciation for design, nature, sustainability,

Industry/Entity Type

Architect

Contact Information for Business Card

See above. The title of Owner or Architect is helpful but not necessary. Minimalism should trump additional information.

Font styles to use
Serif
Sans Serif

Requirements
Must have
• It should look professional. It must use logo
Should not have
• caligraphy, animals, anything that is cute,

```html
<!DOCTYPE html>
<html lang="en">
<head>
<meta charset="utf-8">
<title>Atelier Marrow Architecture – Business Card</title>
<link rel="stylesheet" href="https://fonts.googleapis.com/css2?family=Sorts+Mill+Goudy:ital@0;1&display=swap">
<style>
  :root {
    --green: #087619;
    --white: #ffffff;
    --paper: #fbfbfb;
    --ink: #2b2b2b;
    --stage: #ececec;
  }
  html, body {
    margin: 0;
    width: 1200px;
    height: 586px;
    overflow: hidden;
    background: var(--stage);
    font-family: "Sorts Mill Goudy", Georgia, serif;
  }
  .card {
    position: absolute;
    top: 129px;
    width: 501px;
    height: 301px;
    overflow: hidden;
  }
  .card--front {
    left: 65px;
    background: var(--green);
  }
  .card--back {
    left: 608px;
    background: var(--paper);
  }
  .wordmark {
    position: absolute;
    margin: 0;
    font-weight: 400;
    text-transform: uppercase;
    white-space: nowrap;
  }
  .card--front .wordmark {
    left: 0;
    right: 0;
    top: 136px;
    text-align: center;
    color: var(--white);
    font-size: 17px;
    letter-spacing: 0.2em;
  }
  .card--back .wordmark {
    left: 270px;
    top: 90px;
    color: var(--ink);
    font-size: 10px;
    letter-spacing: 0.18em;
  }
  .wave {
    position: absolute;
    inset: 0;
    width: 100%;
    height: 100%;
  }
  .contact {
    position: absolute;
    left: 28px;
    top: 174px;
    color: var(--white);
  }
  .contact__name {
    margin: 0;
    font-size: 18px;
    font-weight: 400;
    letter-spacing: 0.01em;
    -webkit-text-stroke: 0.4px var(--white);
  }
  .contact__credentials {
    margin: 3px 0 0 3px;
    font-size: 10px;
    font-style: italic;
  }
  .contact__company {
    margin: 30px 0 0;
    font-size: 13.5px;
    -webkit-text-stroke: 0.3px var(--white);
  }
  .contact__address {
    margin: 3px 0 0;
    font-size: 13.5px;
  }
</style>
</head>
<body>
  <section class="card card--front" aria-label="Card front">
    <p class="wordmark">Atelier Marrow Architecture</p>
  </section>

  <section class="card card--back" aria-label="Card back">
    <svg class="wave" viewBox="0 0 627 376" preserveAspectRatio="none" aria-hidden="true">
      <path d="M0,70 C150,35 265,72 385,170 C470,245 545,290 627,276 V376 H0 Z" fill="var(--green)"/>
      <path d="M0,110 C160,80 280,122 390,202 C470,260 540,296 610,296" fill="none" stroke="var(--white)" stroke-width="11" stroke-linecap="round"/>
    </svg>
    <p class="wordmark">Atelier Marrow Architecture</p>
    <div class="contact">
      <h1 class="contact__name">Marcus T. Whitcombe</h1>
      <p class="contact__credentials">AIA, NCARB, LEED AP BD+C</p>
      <p class="contact__company">Atelier Marrow Architecture, Inc.</p>
      <p class="contact__address">728 Holloway Ct. NE Atlanta, GA 30318</p>
    </div>
  </section>
</body>
</html>
```